New Packaging Design for Olives

We are looking for a new packaging design for our product.
- Clear plastic cup container
- 90mm round lid and tapers down to 45mm base
- We do not want a box
- We would like a cardboard wrap around.
Product:
- Pitted Kalamata Olives
- 90g Net
We would like to product to be displayed from top view and side view.
We would like an image of kalamata olives on the packaging
our logo to appear on top and side
the bottom of the packaging to have room for a bar code, ingredients & nutritional panel.
This product is designed to target the accommodation/hotel market and we are wanting a classy looking design to attract mini bar customers.
Attached is an image of the cup & an internal mock up and our company logo.
We need a design that will seamlessly work across a variety of products including salsa, chilli sauce, tomato sauce and others.
Target Market(s)
Hotel Mini bar at 4 to 5 star hotels
Industry/Entity Type
Hotel
Look and feel

```html
<!DOCTYPE html>
<html lang="en">
<head>
<meta charset="utf-8">
<title>Marlowes Pitted Kalamata Olives – Cup Wrap Dieline</title>
<link href="https://fonts.googleapis.com/css2?family=Quicksand:wght@500;600&family=Nunito:wght@400;800&display=swap" rel="stylesheet">
<style>
  :root{
    --stage-light:#f1efef;
    --stage-dark:#c7c5c5;
    --leaf-dark:#0b4a05;
    --leaf-light:#8aad2c;
    --olive-brown:#7b7a1f;
    --ink:#000000;
    --maroon:#140101;
    --brand-yellow:#f7ea1c;
    --brand-red:#d2262c;
    --label-green:#9dbd3c;
    --panel-text:#1a1a1a;
  }
  *{margin:0;padding:0;box-sizing:border-box}
  html,body{width:843px;height:1200px;overflow:hidden}
  body{
    position:relative;
    background:radial-gradient(ellipse at 50% 45%, var(--stage-light) 0%, var(--stage-light) 35%, var(--stage-dark) 100%);
    font-family:"Quicksand",sans-serif;
  }
  .shapes{position:absolute;left:0;top:0;width:843px;height:1200px}
  .abs{position:absolute}

  .brand{
    display:flex;align-items:center;gap:10px;
    font-family:"Nunito",sans-serif;font-weight:800;color:var(--brand-yellow);
    white-space:nowrap;line-height:1;
  }
  .brand-dot{border-radius:50%;background:var(--brand-red);flex:none}

  .label-line{color:var(--label-green);white-space:nowrap;line-height:1;font-weight:500;letter-spacing:1px}
  .net-weight{font-family:"Nunito",sans-serif;font-weight:800;color:var(--label-green);white-space:nowrap;line-height:1}

  .flip{transform:rotate(180deg)}
  .info-column{left:131px;top:50px;width:191px;height:312px;padding:15px 0 0 20px;
    font-size:13px;color:var(--panel-text);line-height:15px;font-family:"Nunito",sans-serif}
  .info-column h3{font-size:13px;font-weight:400;letter-spacing:1px;margin-bottom:6px}
  .info-column p{margin-bottom:24px}
  .contact-box{left:365px;top:77px;width:355px;height:139px;font-family:"Nunito",sans-serif;
    font-size:13px;color:var(--panel-text);line-height:18px}
  .contact-care{left:22px;top:11px}
  .contact-care .gap{height:14px}
  .contact-divider{left:165px;top:10px;width:3px;height:120px;background:var(--ink)}
  .contact-web{left:200px;top:11px}
  .lid-brand{left:365px;top:227px;width:355px;height:135px;display:flex;align-items:center;justify-content:center}

  .side-type{left:67px;top:478px;width:462px;height:254px;transform:rotate(-90deg)}

  .art-side{left:432px;top:462px;width:232px;height:360px;
    background:linear-gradient(160deg, rgba(20,20,28,0.9) 0%, rgba(20,20,28,0.9) 22%, rgba(52,110,28,0.85) 38%, rgba(60,120,30,0.75) 80%, rgba(60,120,30,0.6) 100%)}
  .art-base{left:436px;top:1030px;width:200px;height:105px;
    background:linear-gradient(90deg, rgba(18,18,22,1) 0%, rgba(18,18,22,1) 60%, rgba(60,120,30,0.9) 75%, rgba(110,160,60,0.8) 100%)}
</style>
</head>
<body>
<svg class="shapes" viewBox="0 0 936 1332" aria-hidden="true">
  <rect x="145" y="55" width="655" height="347" fill="var(--leaf-dark)"/>
  <rect x="145" y="55" width="212" height="347" fill="var(--leaf-light)"/>
  <rect x="405" y="85" width="395" height="155" fill="var(--olive-brown)"/>
  <rect x="405" y="252" width="395" height="150" fill="var(--ink)"/>
  <rect x="145" y="415" width="652" height="513" fill="var(--olive-brown)"/>
  <rect x="145" y="415" width="45" height="445" fill="var(--ink)"/>
  <rect x="190" y="415" width="282" height="513" fill="var(--maroon)"/>
  <rect x="472" y="415" width="268" height="47" fill="var(--leaf-dark)"/>
  <rect x="472" y="462" width="268" height="398" fill="var(--leaf-light)"/>
  <rect x="142" y="938" width="655" height="345" fill="var(--leaf-dark)"/>
  <polygon points="612,940 660,940 722,1135 672,1085" fill="var(--leaf-light)"/>
  <polygon points="142,1148 190,1262 142,1283" fill="var(--leaf-light)"/>
  <polygon points="142,938 612,940 672,1085 190,1262 142,1148" fill="var(--ink)"/>
</svg>

<section class="abs info-column flip">
  <h3>INGREDIENTS</h3>
  <p>Lorem ipsum dolor sit<br>amet, consectetur<br>adipiscing elit. Sed<br>molestie neque<br>get lectus pulvinar<br>euismod. Nulla sed<br>magna elit, at lacini</p>
  <h3>NUTRIENTS</h3>
  <p>Lorem ipsum dolor sit<br>amet, consectetur<br>adipiscing elit. Sed</p>
</section>

<section class="abs contact-box flip">
  <div class="abs contact-care">
    <div>Customer Care</div>
    <div>1-800-555 oliv</div>
    <div class="gap"></div>
    <div>Address</div>
    <div>street name</div>
    <div>city</div>
    <div>US</div>
  </div>
  <div class="abs contact-divider"></div>
  <div class="abs contact-web">
    <div>email</div>
    <div>info@marlowes.co</div>
    <div>www.marlowes.co</div>
  </div>
</section>

<div class="abs lid-brand flip">
  <div class="brand" style="font-size:52px"><span class="brand-dot" style="width:26px;height:26px"></span>Marlowes</div>
</div>

<div class="abs art-side" role="img" aria-label="Illustration of a black Kalamata olive on a green olive branch with leaves"></div>

<div class="abs side-type">
  <div class="abs brand" style="left:25px;top:50px;font-size:76px"><span class="brand-dot" style="width:34px;height:34px"></span>Marlowes</div>
  <div class="abs net-weight" style="left:345px;top:158px;font-size:22px">90g NET</div>
  <div class="abs label-line" style="left:21px;top:168px;font-size:30px">Pitted</div>
  <div class="abs label-line" style="left:21px;top:210px;font-size:30px">KALAMATA OLIVES</div>
</div>

<div class="abs label-line" style="left:165px;top:866px;font-size:27px">Pitted</div>
<div class="abs label-line" style="left:165px;top:900px;font-size:27px">KALAMATA OLIVES</div>
<div class="abs net-weight" style="left:165px;top:946px;font-size:20px">90g NET</div>
<div class="abs brand" style="left:180px;top:1000px;height:80px;font-size:74px;transform:rotate(-22deg);transform-origin:left bottom"><span class="brand-dot" style="width:30px;height:30px"></span>Marlowes</div>

<div class="abs art-base" role="img" aria-label="Illustration of a glossy black Kalamata olive with a small leafy sprig"></div>
</body>
</html>
```